Need a business card for a Construction and Remodeling company.
Our company logo is the fleur de lis design as thats the family crust that we use on our logos.
Heres the info it needs:

Brackmore Construction & Remodeling, LLC
Renovations * Restorations

Elwin R. Brackmore
845 North Quarry Road
Harwick Connecticut 06498
(203) 555.0182
CT LIC/REG: 418257

home owners, customers

```html
<!DOCTYPE html>
<html lang="en">
<head>
<meta charset="utf-8">
<title>Brackmore Construction &amp; Remodeling — Business Card</title>
<link rel="stylesheet" href="https://fonts.googleapis.com/css2?family=Archivo+Narrow:wght@700&family=Arimo:wght@400;700&display=swap">
<style>
  :root {
    --bg: #e4e1e1;
    --card: #ffffff;
    --safety-yellow: #f2ea22;
    --ink: #141414;
    --stripe-dark: #3b3b3b;
    --rule: #4a4a36;
    --muted: #6d6d6d;
  }
  * { margin: 0; padding: 0; box-sizing: border-box; }
  html, body { width: 1200px; height: 873px; overflow: hidden; }
  body {
    background: var(--bg);
    font-family: "Arimo", Arial, sans-serif;
    color: var(--ink);
    display: flex;
    flex-direction: column;
    align-items: center;
    justify-content: center;
    gap: 44px;
  }
  .card {
    position: relative;
    width: 560px;
    height: 320px;
    background: var(--card);
    box-shadow: 0 6px 18px rgba(0,0,0,.14);
    overflow: hidden;
  }
  .card__band {
    position: absolute;
    left: 0; right: 0; bottom: 0;
    height: 72px;
    background: var(--safety-yellow);
  }
  .card__band-rule {
    position: absolute;
    left: 150px; right: 40px; top: 20px;
    height: 2px;
    background: var(--rule);
  }
  .card--back .card__band-rule { left: 40px; right: 260px; }
  .hazard-bars {
    position: absolute;
    left: 20px; bottom: 18px;
  }
  .hazard-dashes {
    position: absolute;
    top: 22px; right: 24px;
  }
  .card__content {
    position: absolute;
    left: 0; right: 0; top: 0;
    display: flex;
    flex-direction: column;
    align-items: center;
    text-align: center;
  }
  .brand-mark {
    border: 3px solid var(--ink);
    border-radius: 50%;
  }
  .card--front .card__content { top: 34px; }
  .card--front .brand-mark { width: 104px; height: 104px; margin-bottom: 14px; }
  .card--back .card__content { top: 26px; }
  .card--back .brand-mark { width: 64px; height: 64px; margin-bottom: 8px; }
  .company-name {
    font-family: "Archivo Narrow", "Arial Narrow", sans-serif;
    font-weight: 700;
    letter-spacing: .2px;
  }
  .card--front .company-name { font-size: 24px; }
  .card--back .company-name { font-size: 17px; }
  .tagline {
    text-transform: uppercase;
    color: var(--muted);
    letter-spacing: .5px;
  }
  .card--front .tagline { font-size: 18px; margin-top: 2px; }
  .card--back .tagline { font-size: 13px; margin-top: 1px; }
  .person-name {
    font-weight: 700;
    font-size: 15px;
    margin-top: 9px;
  }
  .contact-lines {
    font-style: normal;
    font-size: 12.5px;
    line-height: 1.35;
    color: var(--muted);
    margin-top: 3px;
  }
  .phone-pill {
    position: absolute;
    right: 26px; bottom: 14px;
    height: 40px;
    padding: 0 18px 0 6px;
    display: flex;
    align-items: center;
    gap: 10px;
    background: var(--ink);
    color: #fff;
    border-radius: 20px;
    font-size: 20px;
    font-weight: 700;
    letter-spacing: .3px;
  }
  .phone-pill__icon {
    width: 28px; height: 28px;
    border-radius: 50%;
    background: #fff;
    display: flex; align-items: center; justify-content: center;
  }
</style>
</head>
<body>

  <section class="card card--front" aria-label="Business card front">
    <svg class="hazard-dashes" width="150" height="20" viewBox="0 0 150 20" aria-hidden="true">
      <g>
        <polygon points="4,20 12,0 22,0 14,20" fill="#f2ea22"/>
        <polygon points="22,20 30,0 40,0 32,20" fill="#3b3b3b"/>
        <polygon points="40,20 48,0 58,0 50,20" fill="#f2ea22"/>
        <polygon points="58,20 66,0 76,0 68,20" fill="#3b3b3b"/>
        <polygon points="76,20 84,0 94,0 86,20" fill="#f2ea22"/>
        <polygon points="94,20 102,0 112,0 104,20" fill="#3b3b3b"/>
        <polygon points="112,20 120,0 130,0 122,20" fill="#f2ea22"/>
        <polygon points="130,20 138,0 148,0 140,20" fill="#3b3b3b"/>
      </g>
    </svg>

    <div class="card__content">
      <div class="brand-mark" aria-hidden="true"></div>
      <h1 class="company-name">Brackmore Construction &amp; Remodeling, LLC</h1>
      <p class="tagline">Renovations | Restorations</p>
    </div>

    <div class="card__band">
      <span class="card__band-rule"></span>
      <svg class="hazard-bars" width="110" height="38" viewBox="0 0 110 38" aria-hidden="true">
        <g fill="#141414">
          <polygon points="0,38 6,0 13,0 7,38"/>
          <polygon points="13,38 19,0 26,0 20,38"/>
          <polygon points="26,38 32,0 39,0 33,38"/>
          <polygon points="39,38 45,0 52,0 46,38"/>
          <polygon points="52,38 58,0 65,0 59,38"/>
          <polygon points="65,38 71,0 78,0 72,38"/>
          <polygon points="78,38 84,0 91,0 85,38"/>
          <polygon points="91,38 97,0 104,0 98,38"/>
        </g>
      </svg>
    </div>
  </section>

  <section class="card card--back" aria-label="Business card back">
    <svg class="hazard-dashes" width="150" height="20" viewBox="0 0 150 20" aria-hidden="true">
      <g>
        <polygon points="4,20 12,0 22,0 14,20" fill="#f2ea22"/>
        <polygon points="22,20 30,0 40,0 32,20" fill="#3b3b3b"/>
        <polygon points="40,20 48,0 58,0 50,20" fill="#f2ea22"/>
        <polygon points="58,20 66,0 76,0 68,20" fill="#3b3b3b"/>
        <polygon points="76,20 84,0 94,0 86,20" fill="#f2ea22"/>
        <polygon points="94,20 102,0 112,0 104,20" fill="#3b3b3b"/>
        <polygon points="112,20 120,0 130,0 122,20" fill="#f2ea22"/>
        <polygon points="130,20 138,0 148,0 140,20" fill="#3b3b3b"/>
      </g>
    </svg>

    <div class="card__content">
      <div class="brand-mark" aria-hidden="true"></div>
      <h2 class="company-name">Brackmore Construction &amp; Remodeling, LLC</h2>
      <p class="tagline">Renovations | Restorations</p>
      <p class="person-name">Elwin R. Brackmore</p>
      <address class="contact-lines">
        845 North Quarry Road<br>
        Harwick Connecticut 06498<br>
        CT LIC/REG: 418257
      </address>
    </div>

    <div class="card__band">
      <span class="card__band-rule"></span>
    </div>

    <p class="phone-pill">
      <span class="phone-pill__icon" aria-hidden="true">
        <svg width="16" height="16" viewBox="0 0 24 24">
          <path d="M6.6 10.8a15.1 15.1 0 0 0 6.6 6.6l2.2-2.2a1 1 0 0 1 1-.25 11.4 11.4 0 0 0 3.6.57 1 1 0 0 1 1 1V20a1 1 0 0 1-1 1A17 17 0 0 1 3 4a1 1 0 0 1 1-1h3.5a1 1 0 0 1 1 1c0 1.250.2 2.46.57 3.6a1 1 0 0 1-.25 1z" fill="#141414"/>
        </svg>
      </span>
      (203) 555.0182
    </p>
  </section>

</body>
</html>
```